Design an attractive wine label for Birch Vale Wines

we need a wine label design, we are an Australian wine exporting company'Birch Vale Wines'. We succeed several pallets in last few months and is going to launch our first container. So it’s time to start our own brands. we will have some wines display in China's shopping mall shelves, so we want to have a catchy label which can attract Chinese eyes immediately. other details you will see in the file i uploaded. The design should include a front and back label.

Target Market(s)

Birch Vale Wines are targeting middle class wine drinkers in 2nd-4th tier Chinese cities.

Colors

Designer to choose colors to be used in the design.

Requirements
Must have
• We’d like something that at first glance is Australian (element, style or color…) but subconsciously connects to the Chinese. Demeanor bearing in mind the demographics targeted across the ranges. We would expect the designs and naming to becoming more formalized as they rise to platinum.
Nice to have
• creative things come out
Should not have
• any dead related word or icon, no number '4' related word or icon, no skull related word or icon, kangaroo (see brand 'Crimson Wing')

```html
<!DOCTYPE html>
<html lang="en">
<head>
<meta charset="utf-8">
<title>Birch Vale Wines – Label Range</title>
<link rel="stylesheet" href="https://fonts.googleapis.com/css2?family=Cinzel:wght@400;500&display=swap">
<style>
  :root {
    --backdrop: #d63a96;
    --label-black: #000000;
    --merlot-accent: #a54bd6;
    --cabernet-accent: #3d9fdc;
    --keyline: #9a9a9a;
    --vintage-ink: #dfe3ff;
    --varietal-ink: #f6dcef;
    --merlot-name: #b565d6;
    --cabernet-name: #7c95e0;
  }
  html, body {
    margin: 0;
    padding: 0;
    width: 1200px;
    height: 879px;
    overflow: hidden;
    background: var(--backdrop);
  }
  .canvas {
    position: relative;
    width: 1200px;
    height: 879px;
  }
  .label {
    position: absolute;
    top: 97px;
    width: 494px;
    height: 689px;
    background: var(--label-black);
  }
  .label p { margin: 0; }
  .label--merlot { left: 100px; --accent: var(--merlot-accent); --name: var(--merlot-name); }
  .label--cabernet { left: 613px; --accent: var(--cabernet-accent); --name: var(--cabernet-name); }

  .label__frame {
    position: absolute;
    inset: 10px;
    border: 4px solid var(--accent);
  }
  .label__keyline {
    position: absolute;
    inset: 21px;
    border: 1.5px solid var(--keyline);
  }
  .label__vintage {
    position: absolute;
    top: 43px;
    left: 0;
    right: 0;
    text-align: center;
    font-family: 'Cinzel', serif;
    font-size: 23px;
    line-height: 1;
    letter-spacing: 0.5px;
    color: var(--vintage-ink);
  }
  .label__artwork {
    position: absolute;
    top: 110px;
    left: 85px;
    width: 300px;
    height: 390px;
  }
  .label--merlot .label__artwork {
    background: linear-gradient(180deg, rgba(138,90,200,0.55) 0%, rgba(180,72,126,0.55) 55%, rgba(210,122,74,0.5) 85%, rgba(0,0,0,0) 100%);
  }
  .label--cabernet .label__artwork {
    background: linear-gradient(180deg, rgba(70,100,224,0.55) 0%, rgba(58,90,214,0.55) 50%, rgba(184,146,46,0.5) 85%, rgba(0,0,0,0) 100%);
  }
  .label__brand {
    position: absolute;
    top: 508px;
    left: 0;
    right: 0;
    text-align: center;
    font-family: 'Cinzel', serif;
    font-weight: 400;
    font-size: 60px;
    line-height: 1;
    letter-spacing: 2px;
    color: var(--name);
  }
  .label__rule {
    position: absolute;
    top: 593px;
    left: 95px;
    width: 330px;
    height: 2px;
    background: linear-gradient(90deg, rgba(0,0,0,0) 0%, var(--accent) 30%, var(--accent) 70%, rgba(0,0,0,0) 100%);
  }
  .label__varietal {
    position: absolute;
    top: 609px;
    left: 0;
    right: 0;
    text-align: center;
    font-family: 'Cinzel', serif;
    font-size: 25px;
    line-height: 1;
    color: var(--varietal-ink);
  }
  .label--cabernet .label__varietal { font-size: 22px; top: 611px; }
</style>
</head>
<body>
<main class="canvas">
  <section class="label label--merlot">
    <div class="label__frame"></div>
    <div class="label__keyline"></div>
    <p class="label__vintage">Vintage 2007</p>
    <div class="label__artwork" role="img" aria-label="Watercolour grape bunch illustration in purple, violet, lime and orange tones"></div>
    <p class="label__brand">Solace</p>
    <div class="label__rule"></div>
    <p class="label__varietal">Merlot</p>
  </section>

  <section class="label label--cabernet">
    <div class="label__frame"></div>
    <div class="label__keyline"></div>
    <p class="label__vintage">Vintage 2007</p>
    <div class="label__artwork" role="img" aria-label="Watercolour grape bunch illustration in cobalt blue and golden yellow tones"></div>
    <p class="label__brand">Solace</p>
    <div class="label__rule"></div>
    <p class="label__varietal">Cabernet Sauvignon</p>
  </section>
</main>
</body>
</html>
```